valtheon construction

i want a construction website something that really epic and eye catchy

we do full Renovation Restoration Construction

if anyone can make my jaw drop there well be a big Reward ,

i have attach my logo

Industry/Entity Type

Construction

Number of Pages Required

4 page

```html
<!DOCTYPE html>
<html lang="en">
<head>
<meta charset="utf-8">
<title>Valtheon Construction</title>
<link rel="stylesheet" href="https://fonts.googleapis.com/css2?family=Open+Sans:wght@400;600;700;800&display=swap">
<style>
:root{
  --red:#b01e1e;
  --red-dark:#8a1010;
  --red-deep:#6e0b0b;
  --ink:#2b2b2b;
  --charcoal:#333638;
  --slate:#45484b;
  --grey-panel:#ececec;
  --grey-text:#666;
  --white:#fff;
}
*{box-sizing:border-box;margin:0;padding:0}
html,body{width:859px;height:1200px;overflow:hidden}
body{font-family:"Open Sans",Arial,sans-serif;color:var(--ink);background:var(--white);position:relative}

.site-header{position:absolute;top:0;left:0;width:859px;height:48px;background:var(--white);display:flex;align-items:center;justify-content:space-between;padding:0 112px 0 118px}
.brand{display:flex;align-items:center;gap:8px}
.brand-mark{width:20px;height:20px;background:var(--red)}
.brand-name{font-weight:800;font-size:14px;color:var(--red);letter-spacing:.5px;line-height:1;text-transform:uppercase}
.main-nav{display:flex;font-size:9.5px;color:var(--ink)}
.main-nav a{color:inherit;text-decoration:none;padding:0 6px;border-left:1px solid #999}
.main-nav a:first-child{border-left:none}

.hero{position:absolute;top:48px;left:0;width:859px;height:330px;background:radial-gradient(ellipse at center,#c22525 0%,#9c1515 70%,#7d0e0e 100%)}
.slider{position:absolute;top:16px;left:118px;width:627px;height:242px;background:var(--white);box-shadow:0 2px 6px rgba(0,0,0,.35)}
.slide-copy{position:absolute;top:22px;left:22px;width:300px}
.slide-title{font-size:19px;font-weight:800;line-height:1.25;color:var(--ink);text-transform:uppercase}
.slide-text{margin-top:12px;font-size:8.5px;line-height:1.65;color:var(--grey-text);text-transform:uppercase}
.slide-media{position:absolute;top:10px;right:14px;width:280px;height:198px;background:linear-gradient(160deg,#e9e5dc 0%,#d8cfbd 55%,#b89a5a 100%)}
.slider-dots{position:absolute;bottom:0;left:0;width:100%;height:24px;background:var(--charcoal);display:flex;justify-content:center;align-items:center;gap:6px}
.slider-dots span{width:7px;height:7px;border-radius:50%;background:#8a8d90}
.slider-dots span.active{background:var(--white)}

.cta-bar{position:absolute;top:272px;left:118px;width:627px;height:40px;background:var(--red-dark);display:flex;align-items:center;justify-content:space-between;padding:0 10px 0 14px;border-top:1px solid #c43a3a}
.cta-text{color:var(--white);font-weight:700;font-size:11.5px}
.cta-button{background:var(--white);color:var(--ink);font-weight:700;font-size:13px;padding:6px 14px;text-decoration:none;display:flex;align-items:center;gap:6px}

.welcome{position:absolute;top:390px;left:118px;width:627px;height:130px}
.welcome-title{font-size:19px;font-weight:800;line-height:1.15;text-transform:uppercase;color:var(--ink);width:300px}
.welcome-title em{font-style:normal;color:var(--red)}
.welcome-text{margin-top:8px;font-size:8.5px;line-height:1.6;color:var(--grey-text);width:300px;text-transform:uppercase}
.btn-dark{display:inline-block;margin-top:8px;background:var(--red-deep);color:var(--white);font-size:8.5px;font-weight:700;padding:4px 10px;text-decoration:none;text-transform:uppercase}
.welcome-media{position:absolute;top:0;right:0;width:300px;height:128px;background:linear-gradient(180deg,#fafafa 0%,#d9d3c6 60%,#a58b5f 100%)}

.features{position:absolute;top:530px;left:110px;width:643px;height:378px;background:var(--grey-panel);display:flex;gap:18px;padding:12px 9px}
.feature{flex:1;background:var(--white);display:flex;flex-direction:column}
.feature-head{background:var(--slate);color:var(--white);font-size:12px;font-weight:600;padding:8px 10px}
.feature-media{margin:10px 10px 0;height:110px}
.media-build{background:linear-gradient(135deg,#c9d3dc 0%,#8b97a3 60%,#5e6770 100%)}
.media-service{background:linear-gradient(135deg,#d7dde2 0%,#a3acb3 55%,#6c5b4c 100%)}
.media-support{background:linear-gradient(135deg,#9ec3e6 0%,#e6c64d 60%,#7c6a3b 100%)}
.feature-title{margin:12px 10px 0;color:var(--red);font-size:11px;font-weight:700}
.feature-text{margin:6px 10px 0;font-size:8.5px;line-height:1.6;color:var(--grey-text)}
.feature .btn-dark{margin:auto 10px 14px;align-self:flex-start;font-size:9px;padding:5px 10px;text-transform:none}

.statement{position:absolute;top:918px;left:0;width:859px;height:190px;background:linear-gradient(180deg,#3a3a3a 0%,#1f1f1f 100%)}
.statement-text{position:absolute;top:22px;left:80px;width:700px;text-align:center;color:var(--white);font-size:22px;font-weight:700;line-height:1.4}
.btn-light{position:absolute;top:122px;left:349px;width:160px;height:44px;background:var(--white);color:var(--red);font-size:22px;font-weight:700;text-decoration:none;display:flex;align-items:center;justify-content:center;gap:8px}
.btn-light svg{width:14px;height:14px}

.site-footer{position:absolute;top:1108px;left:0;width:859px;height:92px;background:#2a2b2c;color:#bbb;font-size:8.5px;padding:16px 118px 0}
.footer-nav{display:flex;color:var(--white)}
.footer-nav a{color:inherit;text-decoration:none;padding:0 6px;border-left:1px solid #777}
.footer-nav a:first-child{border-left:none;padding-left:0}
.copyright{margin-top:8px}
.footer-contact{position:absolute;top:14px;left:500px;line-height:1.6}
.footer-follow{position:absolute;top:14px;left:650px}
.footer-heading{color:#e03a3a;font-weight:700;font-size:10px;margin-bottom:4px}
.social{display:flex;gap:5px}
.social span{width:14px;height:14px;border-radius:50%;background:#5c5f62}
</style>
</head>
<body>

<header class="site-header">
  <div class="brand">
    <span class="brand-mark"></span>
    <span class="brand-name">Valtheon Construction</span>
  </div>
  <nav class="main-nav">
    <a href="#">Home</a><a href="#">About Us</a><a href="#">Services</a><a href="#">Clients</a><a href="#">Careers</a><a href="#">Contact</a>
  </nav>
</header>

<section class="hero">
  <div class="slider">
    <div class="slide-copy">
      <h1 class="slide-title">Committed to superior quality and results.</h1>
      <p class="slide-text">We deliver full renovation, restoration and new construction with careful planning, skilled crews and honest pricing. Every project is built to last and finished on time.</p>
    </div>
    <div class="slide-media" role="img" aria-label="Toy construction worker with hard hat beside an excavator and traffic cones"></div>
    <div class="slider-dots"><span class="active"></span><span></span><span></span><span></span><span></span></div>
  </div>
  <div class="cta-bar">
    <p class="cta-text">Lorem Ipsum is simply dummy text of the printing and typesetting industry.</p>
    <a class="cta-button" href="#">Get Quote</a>
  </div>
</section>

<section class="welcome">
  <h2 class="welcome-title">Welcome to <em>Valtheon</em><br>Construction</h2>
  <p class="welcome-text">From first sketch to final handover, our team manages every stage of your build. We restore older homes, renovate offices and raise new structures with care.</p>
  <a class="btn-dark" href="#">Read More</a>
  <div class="welcome-media" role="img" aria-label="Building materials, tools and bricks arranged around a small model house"></div>
</section>

<section class="features">
  <article class="feature">
    <h3 class="feature-head">Our Construction</h3>
    <div class="feature-media media-build" role="img" aria-label="Steel building framework under construction"></div>
    <h4 class="feature-title">Lorem Ipsum is simply</h4>
    <p class="feature-text">Short description of this service goes here with a few lines of helpful detail for visitors.</p>
    <a class="btn-dark" href="#">Read More</a>
  </article>
  <article class="feature">
    <h3 class="feature-head">Our Services</h3>
    <div class="feature-media media-service" role="img" aria-label="Handshake closing a building agreement"></div>
    <h4 class="feature-title">Lorem Ipsum is simply</h4>
    <p class="feature-text">Short description of this service goes here with a few lines of helpful detail for visitors.</p>
    <a class="btn-dark" href="#">Read More</a>
  </article>
  <article class="feature">
    <h3 class="feature-head">Our Support</h3>
    <div class="feature-media media-support" role="img" aria-label="Site engineers in hard hats reviewing plans outdoors"></div>
    <h4 class="feature-title">Lorem Ipsum is simply</h4>
    <p class="feature-text">Short description of this service goes here with a few lines of helpful detail for visitors.</p>
    <a class="btn-dark" href="#">Read More</a>
  </article>
</section>

<section class="statement" role="img" aria-label="Dark photo of construction workers in hard hats on site">
  <p class="statement-text">Lorem Ipsum is simply dummy text of the printing and type-setting industry. Lorem Ipsum has been the industry's standard dummy text ever since the 1500s,</p>
  <a class="btn-light" href="#">Read More
    <svg viewBox="0 0 14 14" aria-hidden="true"><path d="M3 1 L11 7 L3 13 Z" fill="currentColor"/></svg>
  </a>
</section>

<footer class="site-footer">
  <nav class="footer-nav">
    <a href="#">Home</a><a href="#">About Us</a><a href="#">Services</a><a href="#">Clients</a><a href="#">Careers</a><a href="#">Contact</a>
  </nav>
  <p class="copyright">© 2024 Valtheon Construction. All Rights Reserved.</p>
  <div class="footer-contact">
    <p class="footer-heading">Contact Us</p>
    <p>Phone: +1 555 014 2290</p>
    <p>Email: info@valtheonbuild.com</p>
  </div>
  <div class="footer-follow">
    <p class="footer-heading">Follow Us</p>
    <div class="social"><span></span><span></span><span></span><span></span></div>
  </div>
</footer>

</body>
</html>
```